BRIGHT LEDGER NOW

I'm virtually ready to launch my site, but I have a number of edits and modifications that need to be implemented. More importantly, I'm always looking to improve my site, particularly now that I am making my proverbial "FIRST IMPRESSION." Thus, I'm willing to see if there is someone who can add creativity and perhaps improve what I already have, particularly on the All Important Front Page.

Need extra days to review

```html
<!DOCTYPE html>
<html lang="en">
<head>
<meta charset="utf-8">
<title>Bright Ledger Now — Legal Services</title>
<link href="https://fonts.googleapis.com/css2?family=Ubuntu:wght@400;500;700&family=Open+Sans:wght@400;600;700&display=swap" rel="stylesheet">
<style>
:root{
  --navy:#1d2657;
  --navy-deep:#141b45;
  --red:#b3202b;
  --red-dark:#8e1620;
  --ink:#1f2233;
  --muted:#8a8d99;
  --soft:#f3f5f9;
  --line:#d9dce3;
  --white:#ffffff;
  --black:#050505;
}
*{box-sizing:border-box;margin:0;padding:0}
html,body{width:1200px;height:4696px;overflow:hidden}
body{position:relative;font-family:"Open Sans",sans-serif;color:var(--ink);background:var(--white);font-size:13px}
h1,h2,h3,h4{font-family:"Ubuntu",sans-serif;font-weight:500}
.abs{position:absolute}
.btn{display:inline-flex;align-items:center;gap:14px;background:var(--red);color:var(--white);font-family:"Ubuntu",sans-serif;font-weight:500;font-size:15px;padding:0 24px;height:44px;border-radius:3px}
.btn svg{width:18px;height:18px}
.eyebrow{font-size:12px;font-weight:600;color:var(--red);text-transform:uppercase;letter-spacing:.3px;display:inline-block;border-bottom:1.5px solid var(--red);padding-bottom:2px}

/* top bar */
.topbar{position:absolute;top:0;left:0;width:1200px;height:40px;display:flex;align-items:center;padding:0 92px;font-size:12px;color:var(--navy);font-weight:600}
.topbar .item{display:flex;align-items:center;gap:8px;margin-right:18px}
.topbar svg{width:13px;height:13px;fill:var(--red)}
.topbar .sep{margin-right:18px;color:var(--muted)}
.topbar .social{margin-left:auto;display:flex;gap:14px}
.topbar .social span{width:11px;height:11px;background:#8c93b6;border-radius:2px}

/* hero */
.hero{position:absolute;top:40px;left:0;width:1200px;height:800px;overflow:hidden}
.hero-photo{position:absolute;inset:0;background:linear-gradient(180deg,#242d5c 0%,#2a2c3c 14%,#3a3634 45%,#2f2b2a 75%,#1d1b1c 100%)}
.hero-photo::after{content:"";position:absolute;inset:0;background:radial-gradient(ellipse at 70% 40%,rgba(120,100,90,.35),transparent 60%)}
.brand-mark{position:absolute;top:12px;left:112px;display:flex;align-items:center;gap:10px;color:var(--white);font-family:"Ubuntu",sans-serif;font-weight:500;font-size:11px;line-height:1.2}
.brand-mark .dot{width:58px;height:58px;border-radius:50%;background:var(--red);border:3px solid var(--white)}
.badges{position:absolute;top:26px;left:805px;display:flex;align-items:center;color:var(--white);font-size:12px;font-weight:700;line-height:1.2}
.badges .badge{display:flex;align-items:center;gap:12px}
.badges svg{width:22px;height:22px;stroke:var(--red);fill:none;stroke-width:1.6}
.badges .divider{width:1px;height:38px;background:rgba(255,255,255,.5);margin:0 34px}
.nav{position:absolute;top:88px;left:93px;width:994px;height:66px;background:var(--white);display:flex;align-items:center;font-family:"Ubuntu",sans-serif;font-size:14px;color:var(--ink);border-radius:2px}
.nav a{position:absolute;top:0;height:66px;line-height:66px;text-decoration:none;color:inherit}
.nav a.active{border-bottom:4px solid var(--red);padding:0 22px;left:30px}
.nav .quote{position:absolute;left:815px;top:13px;height:40px;width:154px;border-radius:20px;background:var(--red);color:var(--white);font-size:13px;display:flex;align-items:center;justify-content:center;font-weight:500}
.hero-copy{position:absolute;top:330px;left:0;width:1200px;text-align:center;color:var(--white)}
.hero-copy .kicker{font-size:13px;font-weight:600;letter-spacing:.2px}
.hero-copy h1{font-size:68px;font-weight:700;line-height:90px;margin-top:18px;letter-spacing:.5px}
.hero-copy .btn{margin-top:42px;height:44px;background:var(--red-dark)}
.hero-wave{position:absolute;left:0;top:620px;width:1200px;height:180px}

/* about */
.about{position:absolute;top:840px;left:0;width:1200px;height:607px}
.about-visual{position:absolute;left:95px;top:118px;width:450px;height:444px}
.about-visual .rim{position:absolute;left:0;top:0;width:444px;height:444px;border-radius:50%;background:var(--navy)}
.about-visual .photo{position:absolute;left:14px;top:0;width:440px;height:444px;border-radius:50%;background:radial-gradient(circle at 55% 40%,#6f9ccf 0%,#3f6ea8 40%,#1f3f6d 100%)}
.about-visual .seal{position:absolute;left:336px;top:338px;width:104px;height:104px;border-radius:50%;background:var(--white);display:flex;align-items:center;justify-content:center;box-shadow:0 4px 14px rgba(0,0,0,.15)}
.about-visual .seal span{width:56px;height:56px;border-radius:50%;background:var(--red);border:4px solid var(--navy)}
.about-fade{position:absolute;left:1000px;top:100px;width:360px;height:360px;border-radius:50%;border:26px solid rgba(179,32,43,.07)}
.about-copy{position:absolute;left:613px;top:128px;width:520px}
.about-copy h2{font-size:40px;line-height:55px;color:var(--navy-deep);margin-top:14px}
.about-copy h3{font-size:22px;color:var(--navy-deep);margin-top:18px}
.about-copy p{font-size:12.5px;line-height:22px;color:var(--muted);margin-top:14px}
.about-copy .btn{margin-top:30px}

/* services */
.services{position:absolute;top:1447px;left:0;width:1200px;height:556px;background:var(--soft);text-align:center}
.services .eyebrow{margin-top:43px}
.section-title{font-size:42px;color:var(--navy-deep);margin-top:14px}
.service-grid{position:absolute;top:184px;left:98px;display:flex;gap:28px}
.service{width:314px;height:312px;background:var(--white);border:1px solid #e3e6ec;position:relative;text-align:center;overflow:hidden}
.service.featured{border:none;border-bottom:4px solid var(--red);color:var(--white)}
.service.featured .bg{position:absolute;inset:0;background:linear-gradient(160deg,#55617e,#2f3a5c 60%,#24305a)}
.service .icon{position:absolute;top:60px;left:0;width:100%;display:flex;justify-content:center}
.service .icon svg{width:54px;height:54px;stroke:var(--red);fill:none;stroke-width:3}
.service.featured .icon svg{stroke:var(--white)}
.service h4{position:absolute;top:130px;width:100%;font-size:20px;color:var(--navy-deep)}
.service.featured h4{color:var(--white)}
.service p{position:absolute;top:193px;left:50px;width:214px;font-size:12.5px;line-height:20px;color:var(--muted)}
.service.featured p{color:var(--white)}

/* on call */
.oncall{position:absolute;top:2003px;left:0;width:1200px;height:306px;background:linear-gradient(120deg,#2e2c2e,#4a4644 45%,#2b2a2c);text-align:center}
.oncall h2{position:absolute;top:107px;left:0;width:100%;font-size:34px;line-height:42px;color:var(--white)}
.oncall h2 em{font-style:normal;color:var(--red)}
.oncall-bar{position:absolute;top:2277px;left:350px;width:502px;height:58px;background:var(--white);box-shadow:0 6px 20px rgba(0,0,0,.12);display:flex;align-items:center;justify-content:space-around;font-size:15px;color:var(--navy-deep);padding:0 20px;z-index:2}

/* why */
.why{position:absolute;top:2309px;left:0;width:1200px;height:661px;background:#f7f8fb;text-align:center}
.why .eyebrow{margin-top:82px}
.why .section-title{margin-top:16px}
.hub{position:absolute;left:470px;top:264px;width:256px;height:256px}
.feature{position:absolute;width:220px;text-align:center}
.feature h4{font-size:19px;color:var(--navy-deep)}
.feature p{font-size:12.5px;line-height:20px;color:var(--muted);margin-top:4px}
.feature-icon{position:absolute;width:64px;height:64px;border-radius:50%;background:var(--white);box-shadow:0 6px 16px rgba(29,38,87,.12);display:flex;align-items:center;justify-content:center}
.feature-icon svg{width:32px;height:32px;stroke:var(--red);fill:none;stroke-width:2.4}

/* testimonials */
.reviews{position:absolute;top:2970px;left:0;width:1200px;height:623px;background:linear-gradient(180deg,#2a2320,#3b322d 40%,#251f1d);text-align:center}
.reviews .eyebrow{margin-top:52px;color:var(--white);border-color:var(--white)}
.reviews .section-title{color:var(--white);margin-top:16px}
.review-row{position:absolute;top:213px;left:95px;display:flex;gap:25px}
.review{width:314px;height:270px;position:relative;background:rgba(29,38,87,.9);border:1px solid rgba(255,255,255,.35);color:var(--white)}
.review.light{background:var(--white);color:var(--ink);border:none;border-bottom:4px solid var(--red)}
.review .avatar{position:absolute;top:-35px;left:122px;width:70px;height:70px;border-radius:50%;border:3px solid var(--white);background:linear-gradient(160deg,#e7d3c7,#b88f7d)}
.review h4{position:absolute;top:56px;width:100%;font-family:"Open Sans",sans-serif;font-weight:700;font-size:14px;color:inherit}
.review.light h4{color:var(--navy-deep)}
.review p{position:absolute;top:118px;left:30px;width:254px;font-size:12.5px;line-height:20px}
.review.light p{color:var(--muted)}
.dots{position:absolute;top:528px;left:0;width:100%;display:flex;justify-content:center;align-items:center;gap:10px}
.dots span{width:9px;height:9px;border-radius:50%;border:1px solid #ccc}
.dots span.on{width:22px;height:3px;border:none;border-radius:2px;background:var(--white)}

/* contact */
.contact{position:absolute;top:3593px;left:0;width:1200px;height:640px;background:var(--white)}
.contact h2{position:absolute;top:68px;left:106px;font-size:41px;color:var(--navy-deep);font-weight:700}
.contact h2 span{font-weight:400}
.contact-list{position:absolute;top:138px;left:110px}
.contact-item{display:flex;align-items:flex-start;gap:30px;height:70px}
.contact-item svg{width:42px;height:42px;stroke:var(--red);fill:none;stroke-width:1.5}
.contact-item h4{font-family:"Open Sans",sans-serif;font-weight:700;font-size:13px;color:var(--navy-deep);margin-top:4px}
.contact-item p{font-size:12.5px;color:var(--muted);margin-top:4px}
.form-card{position:absolute;top:3657px;left:600px;width:494px;height:571px;background:var(--white);border-top:5px solid var(--navy);box-shadow:0 10px 30px rgba(0,0,0,.12);padding:52px 36px 0;z-index:3}
.form-card h3{font-size:25px;color:var(--navy-deep)}
.form-row{display:flex;gap:16px;margin-top:26px}
.field{flex:1}
.field label{display:block;font-size:12.5px;font-weight:700;color:var(--navy-deep);margin-bottom:6px}
.field .input{height:42px;border:1px solid #c9ccd4;border-radius:20px;padding:0 24px;display:flex;align-items:center;font-size:12.5px;color:var(--muted)}
.field .area{height:124px;border:1px solid #c9ccd4;border-radius:12px;padding:14px 24px;font-size:12.5px;color:var(--muted)}
.form-card .btn{margin-top:36px;height:46px}
.footer-wave{position:absolute;top:4000px;left:0;width:1200px;height:240px;z-index:1}

/* footer */
.footer{position:absolute;top:4232px;left:0;width:1200px;height:464px;background:var(--black);color:var(--white)}
.footer .mark{position:absolute;left:138px;top:10px;display:flex;align-items:center;gap:12px;font-family:"Ubuntu",sans-serif;font-size:12px;font-weight:500}
.footer .mark .dot{width:92px;height:92px;border-radius:50%;background:var(--red);border:4px solid var(--navy)}
.footer .about-text{position:absolute;left:128px;top:120px;width:290px;font-size:11px;line-height:20px;color:#8a8c96}
.footer .socials{position:absolute;left:128px;top:188px;display:flex;gap:8px}
.footer .socials span{width:30px;height:30px;border-radius:4px;background:#2a2f52}
.footer .socials span:first-child{background:var(--red)}
.footer h5{position:absolute;font-family:"Ubuntu",sans-serif;font-size:14px;font-weight:700}
.footer ul{position:absolute;list-style:none;font-size:12px;color:#8a8c96;line-height:25.5px}
.footer .news-text{position:absolute;left:830px;top:104px;width:250px;font-size:11px;line-height:20px;color:#8a8c96}
.footer .subscribe{position:absolute;left:830px;top:147px;width:246px;height:44px;display:flex}
.footer .subscribe .in{flex:1;background:var(--white);color:#777;font-size:11px;display:flex;align-items:center;padding-left:24px}
.footer .subscribe .go{width:53px;background:var(--red);display:flex;align-items:center;justify-content:center}
.footer .subscribe svg{width:18px;height:18px;stroke:var(--white);fill:none;stroke-width:2.5}
.info-row{position:absolute;top:300px;left:128px;width:960px;height:50px}
.info{position:absolute;display:flex;align-items:center;gap:18px}
.info .ic{width:46px;height:46px;border-radius:50%;background:#2a2f52;display:flex;align-items:center;justify-content:center}
.info .ic.red{background:var(--red)}
.info .ic svg{width:20px;height:20px;fill:var(--white)}
.info h6{font-family:"Open Sans",sans-serif;font-size:14px;font-weight:700}
.info p{font-size:10px;color:#8a8c96;margin-top:2px}
.footer .rule{position:absolute;left:128px;top:400px;width:944px;height:1px;background:#2a2a2a}
.footer .legal{position:absolute;left:0;top:436px;width:100%;text-align:center;font-size:11px;font-weight:700;letter-spacing:.3px}
</style>
</head>
<body>

<header class="topbar">
  <div class="item"><svg viewBox="0 0 24 24"><path d="M6.6 10.8a15 15 0 006.6 6.6l2.2-2.2a1 1 0 011-.25 11.4 11.4 0 003.6.57 1 1 0 011 1V20a1 1 0 01-1 1A17 17 0 013 4a1 1 0 011-1h3.5a1 1 0 011 1 11.4 11.4 0 00.57 3.6 1 1 0 01-.25 1z"/></svg>(+1) 234-567-890</div>
  <span class="sep">|</span>
  <div class="item"><svg viewBox="0 0 24 24"><path d="M2 5h20v14H2z M2 5l10 8 10-8" /></svg>info@company.com</div>
  <div class="item"><svg viewBox="0 0 24 24"><path d="M12 2a7 7 0 00-7 7c0 5 7 13 7 13s7-8 7-13a7 7 0 00-7-7zm0 9.5A2.5 2.5 0 1112 6a2.5 2.5 0 010 5.5z"/></svg>123 ABC DEF</div>
  <div class="social"><span></span><span></span><span></span><span></span></div>
</header>

<section class="hero">
  <div class="hero-photo" role="img" aria-label="Legal team meeting around a table"></div>
  <div class="brand-mark"><span class="dot"></span>BRIGHT LEDGER NOW</div>
  <div class="badges">
    <div class="badge"><svg viewBox="0 0 24 24"><circle cx="12" cy="12" r="9"/><path d="M12 7v5l3 2"/></svg><span>24/7<br>Service</span></div>
    <div class="divider"></div>
    <div class="badge"><svg viewBox="0 0 24 24"><circle cx="12" cy="9" r="5"/><path d="M9 13l-2 8 5-3 5 3-2-8"/></svg><span>Qualified<br>Professionals</span></div>
  </div>
  <nav class="nav">
    <a class="active">Home</a>
    <a style="left:197px">About Us</a>
    <a style="left:334px">Services</a>
    <a style="left:482px">Our Team</a>
    <a style="left:620px">Contact Us</a>
    <span class="quote">Get A Quote</span>
  </nav>
  <div class="hero-copy">
    <div class="kicker">LEGAL SERVICES</div>
    <h1>Navigating Complexity,<br>Delivering Clarity</h1>
    <span class="btn">Contact us <svg viewBox="0 0 24 24" fill="none" stroke="#fff" stroke-width="2"><path d="M4 12h15M13 6l6 6-6 6"/></svg></span>
  </div>
  <svg class="hero-wave" viewBox="0 0 1200 180" preserveAspectRatio="none">
    <path d="M0,18 C250,120 560,165 820,145 C970,133 1100,95 1200,35 L1200,180 L0,180 Z" fill="#fff"/>
    <path d="M230,110 C520,180 900,165 1140,78 C920,145 560,168 230,110 Z" fill="#b3202b"/>
  </svg>
</section>

<section class="about">
  <div class="about-fade"></div>
  <div class="about-visual">
    <div class="rim"></div>
    <div class="photo" role="img" aria-label="Hand touching a network of legal icons: gavel, scales, courthouse"></div>
    <div class="seal"><span></span></div>
  </div>
  <div class="about-copy">
    <span class="eyebrow">Who we are</span>
    <h2>The team you can trust<br>to get the job done</h2>
    <h3>Strategic Advocacy, Lasting Solutions</h3>
    <p>Lorem ipsum dolor sit amet, consectetur adipiscing elit, sed do eiusmod tempor incididunt ut labore et dolore magna aliqua. Ut enim ad minim veniam, quis nos trud exercitation ullamco laboris nisi ut aliquip ex ea commodo consequat. Duis aute irure dolor in reprehenderit in voluptate velit esse cillum dolore eu fugiat nulla pariatur. Excepteur sint occaecat cupidatat non proident, sunt in culpa qui officia deserunt mollit anim id est laborum.</p>
    <span class="btn">Contact us <svg viewBox="0 0 24 24" fill="none" stroke="#fff" stroke-width="2"><path d="M4 12h15M13 6l6 6-6 6"/></svg></span>
  </div>
</section>

<section class="services">
  <span class="eyebrow">Our Services</span>
  <h2 class="section-title">Services We Offer</h2>
  <div class="service-grid">
    <article class="service featured">
      <div class="bg" role="img" aria-label="Lawyer consulting with a client"></div>
      <div class="icon"><svg viewBox="0 0 54 54"><path d="M8 46h38M14 46V34M22 46V26M34 46V22M42 46V14"/><circle cx="30" cy="10" r="4"/></svg></div>
      <h4>Consultation</h4>
      <p>Lorem ipsum dolor sit amet, consectetur adipiscing elit, sed do eiusmod tempor</p>
    </article>
    <article class="service">
      <div class="icon"><svg viewBox="0 0 54 54"><path d="M27 8v38M10 16h34M16 16l-6 14h12zM38 16l-6 14h12zM18 46h18"/></svg></div>
      <h4>Litigation</h4>
      <p>Lorem ipsum dolor sit amet, consectetur adipiscing elit, sed do eiusmod tempor</p>
    </article>
    <article class="service">
      <div class="icon"><svg viewBox="0 0 54 54"><circle cx="27" cy="27" r="20" stroke-dasharray="3 3"/><circle cx="27" cy="27" r="13"/><circle cx="27" cy="27" r="6"/></svg></div>
      <h4>Collection Claims</h4>
      <p>Lorem ipsum dolor sit amet, consectetur adipiscing elit, sed do eiusmod tempor</p>
    </article>
  </div>
</section>

<section class="oncall" role="img" aria-label="Attorneys talking in an office">
  <h2>We're on Call <em>24/7</em> to React Promptly to Your<br>Legal Needs</h2>
</section>
<div class="oncall-bar"><span>+ (001) 234-567-890</span><span>[or]</span><span>info@example.com</span></div>

<section class="why">
  <span class="eyebrow">Why Choose Us</span>
  <h2 class="section-title">Why Choose Us</h2>
  <svg class="hub" viewBox="0 0 256 256">
    <circle cx="128" cy="128" r="126" fill="none" stroke="#1d2657" stroke-width="3"/>
    <circle cx="128" cy="128" r="100" fill="#fff" style="filter:drop-shadow(0 4px 10px rgba(29,38,87,.15))"/>
    <circle cx="128" cy="128" r="48" fill="#b3202b" stroke="#1d2657" stroke-width="5"/>
    <g fill="#fff" stroke="#1d2657" stroke-width="2.5">
      <circle cx="57" cy="24" r="8"/><circle cx="199" cy="24" r="8"/>
      <circle cx="2" cy="128" r="8"/><circle cx="254" cy="128" r="8"/>
      <circle cx="55" cy="232" r="8"/><circle cx="205" cy="228" r="8"/>
    </g>
  </svg>
  <div class="feature-icon" style="left:435px;top:245px"><svg viewBox="0 0 32 32"><circle cx="16" cy="14" r="9"/><path d="M7 22h18v4H7z"/></svg></div>
  <div class="feature-icon" style="left:378px;top:355px"><svg viewBox="0 0 32 32"><circle cx="10" cy="11" r="4"/><path d="M3 24c0-5 3-8 7-8s7 3 7 8M20 10h9M20 16h9M20 22h9"/></svg></div>
  <div class="feature-icon" style="left:428px;top:463px"><svg viewBox="0 0 32 32"><circle cx="16" cy="16" r="11"/><path d="M11 16l4 4 7-8"/></svg></div>
  <div class="feature-icon" style="left:699px;top:245px"><svg viewBox="0 0 32 32"><path d="M26 16a10 10 0 11-4-8M26 5v6h-6"/></svg></div>
  <div class="feature-icon" style="left:756px;top:355px"><svg viewBox="0 0 32 32"><path d="M6 26v-6M12 26v-10M18 26v-6M24 26V10"/><circle cx="24" cy="6" r="2"/></svg></div>
  <div class="feature-icon" style="left:709px;top:463px"><svg viewBox="0 0 32 32"><rect x="5" y="5" width="8" height="8"/><rect x="19" y="19" width="8" height="8"/><path d="M13 9h10v10M9 13v10h10"/></svg></div>

  <div class="feature" style="left:162px;top:242px"><h4>Client Centric</h4><p>Lorem ipsum dolor sit amet,<br>consectetur adipiscing elit,</p></div>
  <div class="feature" style="left:138px;top:361px"><h4>Free Consultation</h4><p>Lorem ipsum dolor sit amet,<br>consectetur adipiscing elit,</p></div>
  <div class="feature" style="left:160px;top:468px"><h4>Minimize Exposure</h4><p>Lorem ipsum dolor sit amet,<br>consectetur adipiscing elit,</p></div>
  <div class="feature" style="left:817px;top:242px"><h4>Attorney Letters</h4><p>Lorem ipsum dolor sit amet,<br>consectetur adipiscing elit,</p></div>
  <div class="feature" style="left:855px;top:361px"><h4>Affordable</h4><p>Lorem ipsum dolor sit amet,<br>consectetur adipiscing elit,</p></div>
  <div class="feature" style="left:817px;top:468px"><h4>Legal Experts</h4><p>Lorem ipsum dolor sit amet,<br>consectetur adipiscing elit,</p></div>
</section>

<section class="reviews" role="img" aria-label="Courtroom with gavel in warm light">
  <span class="eyebrow">Testimonials</span>
  <h2 class="section-title">Clients Reviews</h2>
  <div class="review-row">
    <article class="review light"><div class="avatar" role="img" aria-label="Client portrait"></div><h4>Marcus Hale</h4><p>Lorem ipsum dolor sit amet, consectetur adipiscing elit Lorem ipsum dolor sit amet, consectetur adipiscing elit</p></article>
    <article class="review"><div class="avatar" role="img" aria-label="Client portrait"></div><h4>Marcus Hale</h4><p>Lorem ipsum dolor sit amet, consectetur adipiscing elit Lorem ipsum dolor sit amet, consectetur adipiscing elit</p></article>
    <article class="review"><div class="avatar" role="img" aria-label="Client portrait"></div><h4>Marcus Hale</h4><p>Lorem ipsum dolor sit amet, consectetur adipiscing elit Lorem ipsum dolor sit amet, consectetur adipiscing elit</p></article>
  </div>
  <div class="dots"><span></span><span class="on"></span><span></span></div>
</section>

<section class="contact">
  <h2>Contact Us <span>Today</span></h2>
  <div class="contact-list">
    <div class="contact-item"><svg viewBox="0 0 42 42"><path d="M21 4a10 10 0 00-10 10c0 8 10 18 10 18s10-10 10-18A10 10 0 0021 4z"/><circle cx="21" cy="14" r="4"/><path d="M6 32l-3 7h36l-3-7"/></svg><div><h4>HEAD OFFICE</h4><p>21 Lorem Ipsum, ABC 123</p></div></div>
    <div class="contact-item"><svg viewBox="0 0 42 42"><rect x="4" y="10" width="34" height="24"/><path d="M4 10l17 14 17-14M4 34l13-12M38 34L25 22"/></svg><div><h4>EMAIL ADDRESS</h4><p>21 Lorem Ipsum, ABC 123</p></div></div>
    <div class="contact-item"><svg viewBox="0 0 42 42"><rect x="10" y="4" width="20" height="34" rx="3"/><path d="M17 32h6M34 14a6 6 0 010 12"/></svg><div><h4>CALL US NOW</h4><p>21 Lorem Ipsum, ABC 123</p></div></div>
  </div>
</section>

<svg class="footer-wave" viewBox="0 0 1200 240" preserveAspectRatio="none">
  <path d="M0,240 L0,205 C180,140 400,100 650,80 L1200,60 L1200,240 Z" fill="#050505"/>
  <path d="M60,198 C200,110 400,70 640,60 C430,90 230,130 60,198 Z" fill="#b3202b"/>
</svg>

<form class="form-card">
  <h3>Send Us A Message</h3>
  <div class="form-row">
    <div class="field"><label>First Name</label><div class="input">John</div></div>
    <div class="field"><label>Last Name</label><div class="input">Doe</div></div>
  </div>
  <div class="form-row"><div class="field"><label>Email</label><div class="input">info@company.com</div></div></div>
  <div class="form-row"><div class="field"><label>Message</label><div class="area">Type Your Message</div></div></div>
  <span class="btn">Contact us <svg viewBox="0 0 24 24" fill="none" stroke="#fff" stroke-width="2"><path d="M4 12h15M13 6l6 6-6 6"/></svg></span>
</form>

<footer class="footer">
  <div class="mark"><span class="dot"></span>BRIGHT LEDGER NOW</div>
  <p class="about-text">Lorem ipsum dolor sit amet, consectetur adipiscing elit, sed do eiusmod tempor incididunt ut</p>
  <div class="socials"><span></span><span></span><span></span><span></span></div>

  <h5 style="left:492px;top:48px">Quick Links</h5>
  <ul style="left:492px;top:86px"><li>Home</li><li>Services</li><li>About Us</li><li>Contact</li><li>Blog</li><li>Testimonials</li></ul>
  <ul style="left:629px;top:86px"><li>Cookies Policy</li><li>Terms of Use</li><li>Careers</li><li>Our Team</li><li>More</li></ul>

  <h5 style="left:830px;top:48px">Newsletters</h5>
  <p class="news-text">Lorem ipsum dolor sit amet, consectetur adi elit, sed do eiusmod tempor incididunt ut</p>
  <div class="subscribe"><div class="in">Enter Email Address</div><div class="go"><svg viewBox="0 0 24 24"><path d="M9 5l7 7-7 7"/></svg></div></div>

  <div class="info-row">
    <div class="info" style="left:0"><div class="ic"><svg viewBox="0 0 24 24"><path d="M12 2a7 7 0 00-7 7c0 5 7 13 7 13s7-8 7-13a7 7 0 00-7-7zm0 9.5A2.5 2.5 0 1112 6a2.5 2.5 0 010 5.5z"/></svg></div><div><h6>Address</h6><p>123 Middle Street</p></div></div>
    <div class="info" style="left:240px"><div class="ic red"><svg viewBox="0 0 24 24"><path d="M2 5h20v2l-10 7L2 7zM2 9l10 7 10-7v10H2z"/></svg></div><div><h6>Email Us</h6><p>support@brightledger.com</p></div></div>
    <div class="info" style="left:508px"><div class="ic"><svg viewBox="0 0 24 24"><path d="M6.6 10.8a15 15 0 006.6 6.6l2.2-2.2a1 1 0 011-.25 11.4 11.4 0 003.6.57 1 1 0 011 1V20a1 1 0 01-1 1A17 17 0 013 4a1 1 0 011-1h3.5a1 1 0 011 1 11.4 11.4 0 00.57 3.6 1 1 0 01-.25 1z"/></svg></div><div><h6>Contact Us</h6><p>012(3456) 789 99</p></div></div>
    <div class="info" style="left:736px"><div class="ic"><svg viewBox="0 0 24 24"><path d="M12 2a10 10 0 100 20 10 10 0 000-20zm1 10.4l3.2 2-1 1.6L11 13V6h2z"/></svg></div><div><h6>Opening Hour</h6><p>Mon - Friday 10 am - 5pm</p></div></div>
  </div>
  <div class="rule"></div>
  <div class="legal">BRIGHT LEDGER NOW</div>
</footer>

</body>
</html>
```